plumfable business card

need to upgrade current business card for an online retailer of handmade arts and crafts, please visit plumfable.com.au

need to be artistic professional look

sample layout, contents, logo, are in the attached files

need for 4 people, details for other 2 people to be provided later

```html
<!DOCTYPE html>
<html lang="en">
<head>
<meta charset="utf-8">
<title>PlumFable Business Card</title>
<link rel="stylesheet" href="https://fonts.googleapis.com/css2?family=Open+Sans:wght@300;400&family=Tinos:wght@700&display=swap">
<style>
  :root {
    --backdrop: #e8e8e8;
    --card: #fbfbfb;
    --ink: #2a2a2a;
    --ink-soft: #6f6f6f;
    --accent: #d9342b;
    --rule: #e0746c;
  }
  * { box-sizing: border-box; margin: 0; padding: 0; }
  html, body { width: 1200px; height: 800px; overflow: hidden; }
  body {
    background: var(--backdrop);
    font-family: "Open Sans", Arial, sans-serif;
    color: var(--ink-soft);
    position: relative;
  }
  .card {
    position: absolute;
    width: 525px;
    height: 300px;
    background: var(--card);
    box-shadow: 0 2px 4px rgba(0,0,0,.12), 0 10px 24px rgba(0,0,0,.08);
  }
  .card--back { left: 45px; top: 250px; }
  .card--front { left: 630px; top: 250px; }

  .wordmark {
    font-family: "Tinos", "Times New Roman", serif;
    font-weight: 700;
    color: var(--ink);
    letter-spacing: -0.5px;
    position: absolute;
  }

  /* back side */
  .back__intro {
    position: absolute; left: 40px; top: 34px;
    font-size: 15px; font-weight: 300;
  }
  .back__offer {
    position: absolute; left: 62px; top: 70px;
    list-style: none; font-size: 14.5px; font-weight: 300; line-height: 22px; color: #555;
  }
  .back__offer li::before { content: "\2022\00a0"; }
  .back__ethos {
    position: absolute; left: 40px; top: 200px;
    font-size: 13.5px; font-weight: 400; color: #555;
  }
  .back__rule {
    position: absolute; left: 40px; right: 40px; top: 226px;
    height: 1px; background: var(--rule);
  }
  .card--back .wordmark { right: 40px; top: 234px; font-size: 20px; }

  /* front side */
  .card--front .wordmark { right: 40px; top: 36px; font-size: 40px; }
  .front__rule {
    position: absolute; left: 170px; right: 40px; top: 140px;
    height: 1px; background: var(--rule);
  }
  .services {
    position: absolute; right: 40px; top: 150px; width: 150px;
    font-size: 12px; font-weight: 300; line-height: 15px;
  }
  .services__title { margin-bottom: 6px; }
  .services ul { list-style: none; }
  .services li::before { content: "- "; }

  .person { position: absolute; left: 40px; top: 150px; }
  .person__name {
    font-family: "Tinos", "Times New Roman", serif;
    font-weight: 700; font-size: 32px; color: var(--ink); line-height: 1;
  }
  .person__role { font-size: 12px; font-weight: 300; margin-top: 4px; }
  .contact { list-style: none; margin-top: 8px; font-size: 12px; font-weight: 300; }
  .contact li { display: flex; align-items: center; gap: 8px; height: 20px; }
  .contact svg { width: 14px; height: 14px; fill: var(--accent); }
</style>
</head>
<body>

<section class="card card--back" aria-label="Card back">
  <p class="back__intro">Visit us for exotic hand-made arts &amp; crafts around the globe</p>
  <ul class="back__offer">
    <li>Cashmere fashion items from Nepal</li>
    <li>Thai Traditional Paintings</li>
    <li>Nepali / Tibetan Thangkas</li>
    <li>Lokta / Rice Paper Crafts</li>
    <li>Allo / Cotton / Woollen Items</li>
  </ul>
  <p class="back__ethos">We encourage eco-friendly, sustainable and traditional arts practice.</p>
  <div class="back__rule"></div>
  <div class="wordmark">PlumFable</div>
</section>

<section class="card card--front" aria-label="Card front">
  <div class="wordmark">PlumFable</div>
  <div class="front__rule"></div>
  <div class="services">
    <p class="services__title">We do handicrafts:</p>
    <ul>
      <li>design / promotion</li>
      <li>wholesale / retail</li>
      <li>import / export</li>
    </ul>
  </div>
  <div class="person">
    <h1 class="person__name">Kiran Lama</h1>
    <p class="person__role">Director, PlumFable Australia</p>
    <ul class="contact">
      <li>
        <svg viewBox="0 0 24 24" aria-hidden="true"><path d="M6.6 10.8a15.1 15.1 0 0 0 6.6 6.6l2.2-2.2a1 1 0 0 1 1-.25 11.4 11.4 0 0 0 3.6.57 1 1 0 0 1 1 1V20a1 1 0 0 1-1 1A17 17 0 0 1 3 4a1 1 0 0 1 1-1h3.5a1 1 0 0 1 1 1c0 1.25.2 2.45.57 3.57a1 1 0 0 1-.25 1z"/></svg>
        +61 400 123 456
      </li>
      <li>
        <svg viewBox="0 0 24 24" aria-hidden="true"><path d="M2 5h20v14H2z M2 5l10 8 10-8" fill="var(--accent)"/><path d="M3 6l9 7 9-7" fill="none" stroke="#fff" stroke-width="1.6"/></svg>
        kiran@plumfable.com.au
      </li>
    </ul>
  </div>
</section>

</body>
</html>
```